Vell Harbor Banner Designs

We are looking for 3 Graphic Banners that can be used on our Website and E-mail blasts to our membership base.
See attached file for more information

```html
<!DOCTYPE html>
<html lang="en">
<head>
<meta charset="utf-8">
<title>Vell Harbor Banner</title>
<link rel="stylesheet" href="https://fonts.googleapis.com/css2?family=Open+Sans:wght@400;700&family=Roboto:wght@300;400&display=swap">
<style>
  :root {
    --sky-top: #2457a3;
    --sky-mid: #4f8ad0;
    --sky-low: #6b9fd8;
    --city: #2c5a93;
    --white: #ffffff;
    --panel: rgba(255, 255, 255, 0.86);
    --divider: #5d6f8c;
    --stat-red: #e3232c;
    --stat-label: #4a4f58;
  }
  * { margin: 0; padding: 0; box-sizing: border-box; }
  html, body { width: 1200px; height: 320px; overflow: hidden; background: var(--white); }
  .banner {
    position: relative;
    width: 1200px;
    height: 320px;
    overflow: hidden;
    font-family: "Open Sans", Arial, sans-serif;
  }
  .banner__scene {
    position: absolute;
    inset: 0;
    background:
      linear-gradient(180deg, var(--sky-top) 0%, var(--sky-mid) 38%, var(--sky-low) 62%, var(--city) 78%, #244c7f 100%);
  }
  .brand {
    position: absolute;
    left: 113px;
    top: 64px;
    width: 290px;
    color: var(--white);
  }
  .brand__mark {
    display: flex;
    align-items: center;
    gap: 14px;
    margin-left: 58px;
    height: 100px;
  }
  .brand__dot {
    width: 22px;
    height: 22px;
    border-radius: 50%;
    background: var(--white);
  }
  .brand__name {
    font-size: 60px;
    font-weight: 700;
    line-height: 1;
    letter-spacing: 1px;
  }
  .brand__tagline {
    margin-top: 14px;
    font-size: 17px;
    font-weight: 400;
    white-space: nowrap;
  }
  .brand__city {
    margin-top: 24px;
    margin-left: 70px;
    font-size: 36px;
    font-weight: 700;
    line-height: 1;
  }
  .stats {
    position: absolute;
    left: 505px;
    top: 128px;
    width: 633px;
    height: 88px;
    display: flex;
    background: var(--panel);
  }
  .stat {
    flex: 1;
    display: flex;
    flex-direction: column;
    align-items: center;
    justify-content: center;
    font-family: "Roboto", Helvetica, sans-serif;
  }
  .stat + .stat { border-left: 1px solid var(--divider); }
  .stat__value {
    font-size: 41px;
    font-weight: 300;
    line-height: 1;
    color: var(--stat-red);
  }
  .stat__label {
    margin-top: 6px;
    font-size: 17px;
    font-weight: 300;
    text-transform: uppercase;
    color: var(--stat-label);
  }
</style>
</head>
<body>
  <section class="banner">
    <div class="banner__scene" role="img" aria-label="Photograph of a Gothic parliament building with a central clock tower under a blue sky with clouds, city skyline behind, tinted blue"></div>

    <div class="brand">
      <div class="brand__mark">
        <span class="brand__dot"></span>
        <span class="brand__name">Vell</span>
      </div>
      <p class="brand__tagline">Fostering Entrepreneurship Globally</p>
      <p class="brand__city">Harbor</p>
    </div>

    <div class="stats">
      <div class="stat">
        <span class="stat__value">61</span>
        <span class="stat__label">Chapters</span>
      </div>
      <div class="stat">
        <span class="stat__value">18</span>
        <span class="stat__label">Countries</span>
      </div>
      <div class="stat">
        <span class="stat__value">11261</span>
        <span class="stat__label">Members</span>
      </div>
    </div>
  </section>
</body>
</html>
```